Web Design Project

I want customers to be able to book appointments to get their makeup done and make a deposit and also have a gallery where i put my portfolio images, i want it to be very simple yet elegant.

Target Market(s)

Women ranging from 18-40 that want to get their makeup done

Industry/Entity Type

Makeup

Font styles to use
Sans Serif
Decorative

Requirements
Nice to have
• easy scheduling option and option to pay service in full on website.

```html
<!DOCTYPE html>
<html lang="en">
<head>
<meta charset="utf-8">
<title>YOURLOGO — Makeup Artist</title>
<link href="https://fonts.googleapis.com/css2?family=Roboto+Condensed:wght@400;700&family=Roboto:wght@400;500;700&display=swap" rel="stylesheet">
<style>
:root{
  --pink:#e5125e;
  --pink-deep:#c90f52;
  --pink-bg:#e8195f;
  --dark:#2b2b2b;
  --darker:#242121;
  --panel:#353131;
  --footer:#2e2a2a;
  --text:#444;
  --muted:#6b6b6b;
  --white:#fff;
}
*{margin:0;padding:0;box-sizing:border-box}
html,body{width:1200px;height:3097px;overflow:hidden}
body{position:relative;background:var(--white);font-family:"Roboto",Arial,sans-serif;color:var(--text)}
.abs{position:absolute}

/* top bar */
.topbar{left:0;top:0;width:1200px;height:60px;background:var(--dark);color:var(--white)}
.topbar .welcome{left:95px;top:22px;font:700 14px "Roboto Condensed",sans-serif;letter-spacing:.3px}
.topbar nav{left:635px;top:22px;display:flex;gap:34px;font:700 14px "Roboto Condensed",sans-serif}
.topbar .search{left:1014px;top:0;width:186px;height:60px;background:var(--pink)}

/* header */
.logo{left:95px;top:92px;font:700 50px "Roboto Condensed",sans-serif;color:var(--pink);letter-spacing:-.5px}
.header-links{left:776px;top:110px;font:500 15px "Roboto",sans-serif;color:#222;display:flex;gap:18px}

/* hero */
.hero{left:0;top:180px;width:1200px;height:440px;background:linear-gradient(90deg,#b99a88 0%,#e9d9cf 22%,#e2d4ce 40%,#d6c8c8 70%,#cbbcbe 100%)}
.tag{background:var(--pink);color:var(--white);font-family:"Roboto Condensed",sans-serif;font-weight:700;text-align:center;white-space:nowrap;overflow:hidden}
.tag-small{left:705px;top:297px;width:230px;height:51px;font-size:34px;line-height:51px}
.tag-big{left:612px;top:359px;width:490px;height:80px;font-size:47px;line-height:80px}
.btn-trap{display:flex;align-items:center;justify-content:center;color:var(--white);font:700 26px "Roboto Condensed",sans-serif}
.btn-trap svg{position:absolute;left:0;top:0}
.btn-trap span{position:relative}

/* section headings */
.boxed{border:2px solid #555;text-align:center;font:700 26px "Roboto Condensed",sans-serif;color:#333;display:flex;align-items:center;justify-content:center}
.boxed.light{border-color:var(--white);color:var(--white)}

.intro{left:134px;top:790px;width:932px;font-size:12.5px;line-height:25px;text-align:center;color:var(--muted)}
.portfolio-img{top:895px;width:287px;height:388px}

/* why */
.why{left:0;top:1538px;width:1200px;height:637px;background:radial-gradient(circle at 30% 40%,#ee3c77 0%,var(--pink-bg) 45%,#d80f55 100%)}
.feature{width:320px;height:170px;color:var(--white)}
.feature .num{position:absolute;left:0;top:0;width:46px;height:46px;background:var(--white);color:var(--pink);font:700 34px/46px "Roboto Condensed",sans-serif;text-align:center}
.feature h3{position:absolute;left:64px;top:12px;font:700 22px "Roboto Condensed",sans-serif}
.feature .rule{position:absolute;left:64px;top:44px;width:50px;height:3px;background:var(--white)}
.feature p{position:absolute;left:0;top:62px;width:310px;font-size:13.5px;line-height:24px}
.feature .more{position:absolute;left:0;top:142px;font:700 15px "Roboto Condensed",sans-serif}

/* testimonial */
.testimonial-img{left:137px;top:2363px;width:198px;height:220px;background:linear-gradient(135deg,#8a6048,#d9b393 55%,#b8876a)}
.t-name{left:364px;top:2393px;font:500 19px "Roboto Condensed",sans-serif;color:#333}
.t-rule{left:364px;top:2424px;width:80px;height:3px;background:var(--pink)}
.t-text{left:364px;top:2443px;width:300px;font-size:14px;line-height:25px;color:var(--muted)}
.product-img{left:717px;top:2363px;width:346px;height:220px;background:linear-gradient(135deg,#3a2c28,#a88a7a 50%,#e0cfc6)}

/* footer */
.footer{left:0;top:2645px;width:1200px;height:355px;background:var(--footer)}
.fcol{top:2645px;width:336px;height:315px;background:var(--panel);color:#ddd}
.fcol .head{height:98px;background:var(--pink);color:var(--white);font:700 26px/98px "Roboto Condensed",sans-serif;text-align:center}
.fcol .head.deep{background:var(--pink-deep)}
.fcol .dash{width:48px;height:2px;background:#ccc;margin:34px auto 0}
.fcol p{font-size:13.5px;line-height:25px;text-align:center;margin:16px 30px 0}
.fcol .fbtn{display:block;width:132px;height:38px;border:2px solid #ddd;margin:22px auto 0;text-align:center;font:700 14px/34px "Roboto Condensed",sans-serif;color:var(--white)}
.news-row{display:flex;margin:22px 34px 0}
.news-row .field{flex:1;height:38px;background:var(--white)}
.news-row .send{width:80px;height:38px;background:#4a4646;border:1px solid #999;color:var(--white);font:700 15px/36px "Roboto Condensed",sans-serif;text-align:center}

.bottombar{left:0;top:3000px;width:1200px;height:97px;background:var(--darker);color:#ddd;font-size:13.5px}
.copyright{left:95px;top:40px}
.copyright b{color:var(--white)}
.footer-nav{left:448px;top:40px;display:flex;gap:19px}
.social{left:921px;top:34px;display:flex;gap:12px}
.social span{width:27px;height:27px;display:block}
</style>
</head>
<body>

<header class="abs topbar">
  <div class="abs welcome">WELCOME TO OUR SITE VISITORS</div>
  <nav class="abs"><span>HOME</span><span>ABOUT ME</span><span>MY SERVICES</span><span>CONTACT</span></nav>
  <div class="abs search">
    <svg width="186" height="60" viewBox="0 0 186 60"><circle cx="90" cy="28" r="5" fill="none" stroke="#fff" stroke-width="2"/><line x1="94" y1="32" x2="98" y2="36" stroke="#fff" stroke-width="2"/></svg>
  </div>
</header>

<div class="abs logo">YOURLOGO</div>
<div class="abs header-links"><span>BOOK APPOINTMENTS</span><span>|</span><span>MAKE A DEPOSIT</span></div>

<section class="abs hero" role="img" aria-label="Portrait of a woman with finished makeup"></section>
<div class="abs tag tag-small">DOLOREMQUE</div>
<div class="abs tag tag-big">IAM AUT ASPERNATUR</div>
<a class="abs btn-trap" style="left:753px;top:449px;width:207px;height:51px">
  <svg width="207" height="51"><polygon points="0,0 207,0 190,51 17,51" fill="#3c3c3c"/></svg>
  <span>READ MORE</span>
</a>

<div class="abs boxed" style="left:485px;top:686px;width:230px;height:60px">MY PORTFOLIO</div>
<p class="abs intro">Lorem ipsum dolor sit amet rem eos illo omnis aut aperiam ab ipsam ipsa odit aut aperiam aut aspernatur veritatis unde sed enim accusantium laudantium sunt perspiciatis ipsam sed doloremque ipsam dolores totam unde aut illo aut veritatis explicabo dicta quia dicta veritatis dicta sunt quasi eaque rem</p>

<div class="abs portfolio-img" style="left:126px;background:linear-gradient(160deg,#6e4a38,#c9a48e 55%,#e8d6ca)" role="img" aria-label="Portfolio photo: bridal makeup with curled hair"></div>
<div class="abs portfolio-img" style="left:457px;background:linear-gradient(160deg,#d9cfc2,#a48a70 55%,#efe8df)" role="img" aria-label="Portfolio photo: natural makeup with knit scarf"></div>
<div class="abs portfolio-img" style="left:787px;background:linear-gradient(160deg,#9a7160,#e3cfc4 55%,#f2ebe6)" role="img" aria-label="Portfolio photo: editorial makeup with pearl necklace"></div>

<a class="abs btn-trap" style="left:493px;top:1380px;width:212px;height:55px">
  <svg width="212" height="55"><polygon points="0,0 212,0 194,55 18,55" fill="#3c3c3c"/></svg>
  <span>READ MORE</span>
</a>

<section class="abs why"></section>
<div class="abs boxed light" style="left:436px;top:1620px;width:328px;height:57px">WHAT YOU CHOOSE ME</div>

<div class="abs feature" style="left:95px;top:1742px"><div class="num">1</div><h3>AMET VOLUPTATEM</h3><div class="rule"></div><p>Lorem ipsum dolor sit amet rem illo omnis aperiam ab ipsam ipsa odit aut aperiam aspernatur veritatis unde enim accusantium laudantium sunt</p><div class="more">READ MORE</div></div>
<div class="abs feature" style="left:452px;top:1742px"><div class="num">2</div><h3>AMET VOLUPTATEM</h3><div class="rule"></div><p>Lorem ipsum dolor sit amet rem illo omnis aperiam ab ipsam ipsa odit aut aperiam aspernatur veritatis unde enim accusantium laudantium sunt</p><div class="more">READ MORE</div></div>
<div class="abs feature" style="left:805px;top:1742px"><div class="num">3</div><h3>AMET VOLUPTATEM</h3><div class="rule"></div><p>Lorem ipsum dolor sit amet rem illo omnis aperiam ab ipsam ipsa odit aut aperiam aspernatur veritatis unde enim accusantium laudantium sunt</p><div class="more">READ MORE</div></div>
<div class="abs feature" style="left:95px;top:1950px"><div class="num">4</div><h3>AMET VOLUPTATEM</h3><div class="rule"></div><p>Lorem ipsum dolor sit amet rem illo omnis aperiam ab ipsam ipsa odit aut aperiam aspernatur veritatis unde enim accusantium laudantium sunt</p><div class="more">READ MORE</div></div>
<div class="abs feature" style="left:452px;top:1950px"><div class="num">5</div><h3>AMET VOLUPTATEM</h3><div class="rule"></div><p>Lorem ipsum dolor sit amet rem illo omnis aperiam ab ipsam ipsa odit aut aperiam aspernatur veritatis unde enim accusantium laudantium sunt</p><div class="more">READ MORE</div></div>
<div class="abs feature" style="left:805px;top:1950px"><div class="num">6</div><h3>AMET VOLUPTATEM</h3><div class="rule"></div><p>Lorem ipsum dolor sit amet rem illo omnis aperiam ab ipsam ipsa odit aut aperiam aspernatur veritatis unde enim accusantium laudantium sunt</p><div class="more">READ MORE</div></div>

<div class="abs boxed" style="left:273px;top:2245px;width:258px;height:57px">WHAT THEY SAYS</div>
<div class="abs boxed" style="left:748px;top:2245px;width:284px;height:57px">HIGHLIGHTS PRODUCT</div>

<div class="abs testimonial-img" role="img" aria-label="Client portrait with long wavy hair"></div>
<div class="abs t-name">MAYA DOE, 25 YO</div>
<div class="abs t-rule"></div>
<p class="abs t-text">Lorem ipsum dolor sit amet rem eos illo omnis aut aperiam ab ipsam ipsa odit aut aperiam aspernatur veritatis unde accusantium sunt perspiciatis ipsam sed doloremque ....</p>
<div class="abs product-img" role="img" aria-label="Makeup artist applying powder to a client"></div>

<footer class="abs footer"></footer>
<div class="abs fcol" style="left:95px"><div class="head">ABOUT US</div><div class="dash"></div><p>Lorem ipsum dolor sit amet omnis aperiam ab ipsam ipsa odit aut aperiam aspernatur veritatis unde enim accusantium laudantium</p><a class="fbtn">READ MORE</a></div>
<div class="abs fcol" style="left:431px"><div class="head deep">COMPANY ADDRESS</div><div class="dash"></div><p>Lorem ipsum dolor sit amet omnis aperiam ab ipsam ipsa odit aut aperiam aspernatur veritatis unde enim accusantium laudantium</p><a class="fbtn">READ MORE</a></div>
<div class="abs fcol" style="left:767px"><div class="head">NEWSLETTER</div><div class="dash"></div><p>Lorem ipsum dolor sit amet omnis aperiam</p><div class="news-row"><div class="field"></div><div class="send">SEND</div></div><p>ab ipsam ipsa odit aut aperiam aspernatur veritatis unde enim accusantium</p></div>

<div class="abs bottombar">
  <div class="abs copyright">© 2014 <b>YOUR COMPANY</b>. ALL RIGHTS RESERVED.</div>
  <div class="abs footer-nav"><span>ABOUT US</span><span>TERM AND USE</span><span>PRIVACY POLICY</span><span>FAQS</span><span>CONTACT US</span></div>
  <div class="abs social"><span style="background:#3b5998"></span><span style="background:#1da1f2"></span><span style="background:#d6402f"></span><span style="background:#0e76a8"></span><span style="background:#cb2027"></span></div>
</div>

</body>
</html>
```